Website for Private Psychologist

DO NOT CONTACT ME PRIVATELY

I am a Psychologist offering psychotherapy for individuals and couples, and clinical consultation and training and education for mental and medical health professionals and agencies.

I need a redesign of my website

5 Pages (content is attached for each page)
Home
Jungian Psychotherapy
Clinical Consultation & Professional Development
Curriculum Vitae & Publications
Practice Policies and Forms

Designs can be based on these style websites
https://lqmindcare.info; https://pdtarn.org/; https://dorabellcroftcounselling.com/

Design Concepts
Minimalist Layout: Clean and uncluttered layout with generous white space, allowing the content and visuals to stand out'

Keep a linear, uncluttered, professional design.

Please use only royalty free images and google fonts. Please provide links to any stock images used to verify license.

Target Market(s)

private individual or couples seeking psychotherapy

Industry/Entity Type

Psychotherapy

Number of Pages Required

5+ page

Requirements
Should not have
• No search feature

```html
<!DOCTYPE html>
<html lang="en">
<head>
<meta charset="utf-8">
<title>Elliot Marlowe, Psy.D. Psychotherapy</title>
<link href="https://fonts.googleapis.com/css2?family=Lora:wght@400;500&family=Lato:wght@400;700&display=swap" rel="stylesheet">
<style>
:root{
  --navy:#2c3a55;
  --blue:#5082c3;
  --slate:#434f63;
  --ink:#2f3440;
  --muted:#5b6170;
  --pale:#eef2f9;
  --panel:#f4f7f5;
  --white:#ffffff;
}
*{box-sizing:border-box;margin:0;padding:0}
html,body{width:1200px;height:4345px;overflow:hidden}
body{position:relative;background:var(--white);font-family:'Lato',sans-serif;color:var(--ink)}
.serif{font-family:'Lora',serif;font-weight:400}
.abs{position:absolute}
.eyebrow{font-size:12px;letter-spacing:2.5px;text-transform:uppercase}
.btn{position:absolute;display:flex;align-items:center;justify-content:center;font-size:11px;letter-spacing:.6px}
.photo{position:absolute}

/* top bar + nav */
.topbar{left:0;top:0;width:1200px;height:25px;background:var(--navy)}
.topbar .lic{right:215px;top:7px;font-size:8px;color:#c9d2e3}
.topbar .book{left:969px;top:0;width:157px;height:25px;background:var(--blue);color:#fff;font-size:8px;letter-spacing:1px}
.nav{left:0;top:25px;width:1200px;height:70px;background:#fff}
.logo{left:76px;top:45px;font-size:22px;color:var(--navy)}
.logo b{font-weight:400;color:var(--blue)}
.menu{right:74px;top:52px;display:flex;gap:20px;font-size:11px;color:var(--ink)}

/* hero */
.hero{left:0;top:95px;width:1200px;height:570px;background:linear-gradient(120deg,#3d5a86 0%,#5a76a0 40%,#3a5175 75%,#2c3f5f 100%)}
.hero-text{left:0;width:1200px;text-align:center;color:#fff}
.dots{display:flex;gap:8px;justify-content:center}
.dots i{display:block;width:20px;height:4px;border:1px solid #fff;border-radius:2px}
.dots i.on{background:var(--blue);border-color:var(--blue)}

/* about */
.about-p{left:164px;top:918px;width:420px;font-size:11.5px;line-height:22px;color:var(--ink)}

/* services */
.card-t{font-size:22px;line-height:30px}
.card-p{font-size:10.5px;line-height:20px}

/* calendar */
.cal{left:262px;top:2748px;width:349px;background:#fff}
.cal-head{height:46px;background:var(--navy);color:#fff;display:flex;align-items:center;justify-content:space-between;padding:0 20px;font-family:'Lora',serif;font-size:15px}
.cal-days,.cal-grid{display:grid;grid-template-columns:repeat(7,1fr)}
.cal-days{height:28px;background:var(--slate);color:#fff;font-size:9.5px;align-items:center;text-align:center;letter-spacing:.5px}
.cal-grid div{height:50px;display:flex;align-items:center;justify-content:center;font-size:10px;border-right:1px solid #e3e7ee;border-bottom:1px solid #e3e7ee;color:var(--ink)}
.cal-grid .out{background:#eef1f5;color:#7d8696}
.cal-grid .sel{background:var(--blue);color:#fff}

/* resources */
.res{position:absolute;top:3340px;width:333px;height:348px;background:var(--pale)}
.res .img{position:absolute;left:0;top:0;width:333px;height:171px}
.res h3{position:absolute;top:208px;width:100%;text-align:center;font-family:'Lora',serif;font-weight:500;font-size:17px}
.res .btn{left:91px;top:262px;width:150px;height:44px;background:var(--blue);color:#fff}

/* contact */
.contact{left:0;top:3853px;width:1200px;height:492px;background:var(--blue)}
.ci{left:174px;color:#fff;display:flex;gap:14px}
.ci .ic{width:22px;height:22px;border-radius:50%;background:#fff;display:flex;align-items:center;justify-content:center;flex:none}
.ci small{display:block;font-size:8.5px;margin-bottom:6px}
.ci span{font-size:10.5px;line-height:16px}
.hours{left:518px;top:4026px;width:377px;height:253px;background:var(--panel);padding:28px 35px}
.hours h4{font-family:'Lora',serif;font-weight:400;font-size:15px;margin-bottom:22px}
.hours .row{display:flex;justify-content:space-between;font-size:10.5px;color:var(--muted);padding:0 0 15px;margin-bottom:15px;border-bottom:1px solid #dfe5e2}
.hours .row:last-child{border:none}
</style>
</head>
<body>

<div class="abs topbar">
  <svg class="abs" style="left:68px;top:6px" width="10" height="13" viewBox="0 0 10 13"><path d="M5 0a4.5 4.5 0 0 0-4.5 4.5C.5 8 5 13 5 13s4.5-5 4.5-8.5A4.5 4.5 0 0 0 5 0z" fill="#fff"/><circle cx="5" cy="4.5" r="1.6" fill="#2c3a55"/></svg>
  <div class="abs lic">California Licensed Psychologist PSY 48211</div>
  <div class="btn book">BOOK AN APPOINTMENT</div>
</div>

<div class="abs nav"></div>
<div class="abs logo serif">Elliot<b>Marlowe</b></div>
<nav class="abs menu">
  <span>Home</span><span>Jungian Psychotherapy</span><span>Clinical Consultation &amp; Professional Development</span><span>CV &amp; Publications</span><span>Practice Policies &amp; Forms</span>
</nav>

<section class="abs hero" role="img" aria-label="Therapy room with a counsellor talking with a client, tinted blue"></section>
<div class="abs hero-text eyebrow" style="top:262px;font-size:11px">Psychotherapy and Counselling</div>
<h1 class="abs hero-text serif" style="top:288px;font-size:47px;line-height:56px">Welcome to Elliot Marlowe,<br>Psy.D. Psychotherapy</h1>
<div class="abs hero-text" style="top:418px;font-size:21px">Empowering Your Journey Towards Emotional Well-being</div>
<div class="btn" style="left:503px;top:483px;width:194px;height:42px;background:var(--blue);color:#fff">BOOK AN APPOINTMENT</div>
<div class="abs dots" style="left:0;top:636px;width:1200px"><i class="on"></i><i></i><i></i></div>

<!-- about -->
<div class="abs eyebrow" style="left:164px;top:830px;font-size:11px;color:var(--blue)">About Me</div>
<h2 class="abs serif" style="left:164px;top:853px;font-size:32px;color:var(--ink)">Elliot Marlowe, <span style="color:var(--blue)">Psy.D.</span></h2>
<p class="abs about-p">I am a licensed clinical psychologist with a private practice in San Francisco. I provide treatment for adolescents, adults, and couples, as well as clinical consultation and training for mental and medical health professionals and agencies. I am also Adjunct Faculty with the Harbor Institute Counseling Psychology M.A. Program.</p>
<div class="btn" style="left:164px;top:1058px;width:133px;height:36px;background:var(--slate);color:#fff;font-size:10px">CONTACT ME</div>
<div class="photo" style="left:678px;top:790px;width:358px;height:365px;background:var(--blue)"></div>
<div class="photo" role="img" aria-label="Portrait of the psychologist in a dark suit" style="left:780px;top:755px;width:150px;height:400px;background:linear-gradient(180deg,#4a6fa3 0%,#2a2f3a 40%,#1f232b 100%);border-radius:60px 60px 0 0;opacity:.55"></div>

<!-- services -->
<div class="abs eyebrow" style="left:0;width:1200px;text-align:center;top:1258px;font-size:13px;color:var(--blue)">Services</div>
<h2 class="abs serif" style="left:0;width:1200px;text-align:center;top:1286px;font-size:33px">Empowering Transformation &amp; Elevating <span style="color:var(--blue)">Clinical Excellence</span></h2>
<div class="abs" style="left:0;width:1200px;text-align:center;top:1346px;font-size:14px">Services That Can Change Your Life and Enhance Your Impact</div>

<div class="photo" role="img" aria-label="Therapist showing a smiley card to a young client" style="left:74px;top:1413px;width:518px;height:292px;background:linear-gradient(110deg,#d8d3cc,#ece9e4 50%,#b9ada0)"></div>
<div class="abs" style="left:74px;top:1705px;width:518px;height:273px;background:#f3f2f0"></div>
<h3 class="abs serif card-t" style="left:116px;top:1738px">Jungian Psychotherapy &amp; Consultation</h3>
<p class="abs card-p" style="left:116px;top:1793px;width:450px">I practice depth-oriented psychotherapy and tailor my approach to the individual or couple seeking treatment. I have experience treating a range of psychological issues including depression, anxiety, and relationship and job dissatisfaction as well as life transition issues such as college and graduate school stress, pre-marital counseling, and issues related to identity and sexuality.</p>
<div class="btn" style="left:116px;top:1920px;width:129px;height:32px;border:1px solid var(--blue);color:var(--blue);background:#fff">Read More</div>

<div class="photo" role="img" aria-label="Counsellor listening to a young woman in a bright room" style="left:606px;top:1413px;width:520px;height:292px;background:linear-gradient(110deg,#c9c3bd,#eaeaea 45%,#d9d6d0)"></div>
<div class="abs" style="left:606px;top:1705px;width:520px;height:273px;background:var(--blue)"></div>
<h3 class="abs serif card-t" style="left:651px;top:1725px;width:440px;color:#fff">Clinical Consultation &amp; Professional Development</h3>
<p class="abs card-p" style="left:651px;top:1793px;width:420px;color:#fff">I provide professional consultation for pre- and post-licensed psychotherapists on a range of clinical issues including substance use disorder assessment and treatment; motivational interviewing; and treatment issues specific to LGBT clients. For Psychology Interns and trainees, I offer clinical supervision, case consultation, and professional development.</p>
<div class="btn" style="left:651px;top:1920px;width:130px;height:32px;background:#fff;color:var(--blue)">Read More</div>

<!-- testimonials -->
<section class="abs" role="img" aria-label="Woman sitting on stairs, dimmed background" style="left:0;top:2041px;width:1200px;height:481px;background:linear-gradient(90deg,#3f4a5d 0%,#424d60 60%,#55606f 80%,#414c5e 100%)"></section>
<div class="abs eyebrow" style="left:0;width:1200px;text-align:center;top:2167px;font-size:11px;color:#e3e7ee">Testimonials</div>
<h2 class="abs serif" style="left:0;width:1200px;text-align:center;top:2193px;font-size:33px;color:#fff">What Clients Say</h2>
<p class="abs serif" style="left:180px;width:840px;text-align:center;top:2250px;font-size:19.5px;line-height:25px;color:#fff">"Dr. Marlowe's Jungian Psychotherapy has been a life-changing experience for me. Through our sessions, I've gained a deeper understanding of myself and my emotions, helping me navigate through challenging times with newfound strength and clarity. His empathetic and personalized approach truly makes a difference!"</p>
<div class="abs" style="left:0;width:1200px;text-align:center;top:2369px;font-size:10px;color:#e3e7ee">Nora Ellis, CA, USA</div>
<div class="abs dots" style="left:0;top:2451px;width:1200px"><i></i><i class="on"></i><i></i></div>

<!-- appointment -->
<div class="photo" role="img" aria-label="Office with a potted plant and wooden cabinet" style="left:74px;top:2584px;width:697px;height:601px;background:linear-gradient(180deg,#c9c7c2 0%,#b9b6ae 55%,#44506a 80%,#3a4662 100%)"></div>
<div class="photo" role="img" aria-label="Therapy room with bookshelf by a window" style="left:782px;top:2584px;width:342px;height:292px;background:linear-gradient(160deg,#c8b59a,#e3dccf 45%,#9c7a56)"></div>
<div class="photo" role="img" aria-label="Corner with a small table and armchair" style="left:782px;top:2893px;width:342px;height:292px;background:linear-gradient(160deg,#e9e2d6,#d8cbb8 60%,#a88660)"></div>
<div class="abs eyebrow" style="left:263px;top:2673px;font-size:10px;color:#fff">Get a Consultation</div>
<h2 class="abs serif" style="left:262px;top:2690px;font-size:33px;color:#fff">Book an Appointment</h2>
<div class="abs cal">
  <div class="cal-head">
    <svg width="10" height="12" viewBox="0 0 10 12"><path d="M7 1 2 6l5 5" fill="none" stroke="#fff" stroke-width="2"/></svg>
    <span>August 2023</span>
    <svg width="10" height="12" viewBox="0 0 10 12"><path d="m3 1 5 5-5 5" fill="none" stroke="#fff" stroke-width="2"/></svg>
  </div>
  <div class="cal-days"><span>SUN</span><span>MON</span><span>TUE</span><span>WED</span><span>THU</span><span>FRI</span><span>SAT</span></div>
  <div class="cal-grid">
    <div class="out">30</div><div class="out">31</div><div>1</div><div>2</div><div>3</div><div>4</div><div>5</div>
    <div>6</div><div>7</div><div>8</div><div>9</div><div>10</div><div>11</div><div>12</div>
    <div>13</div><div>14</div><div>15</div><div class="sel">16</div><div>17</div><div>18</div><div>19</div>
    <div>20</div><div>21</div><div>22</div><div>23</div><div>24</div><div>25</div><div>26</div>
    <div>27</div><div>28</div><div>29</div><div>30</div><div class="out">1</div><div class="out">2</div><div class="out">3</div>
  </div>
</div>

<!-- resources -->
<h2 class="abs serif" style="left:0;width:1200px;text-align:center;top:3266px;font-size:33px">Useful Resources</h2>
<div class="res" style="left:83px">
  <div class="img" role="img" aria-label="Hand holding a printed resume" style="background:linear-gradient(120deg,#d9d4cc,#eef0f2 55%,#a8b4c2)"></div>
  <h3>Curriculum Vitae</h3><div class="btn">Read more</div>
</div>
<div class="res" style="left:434px">
  <div class="img" role="img" aria-label="Open book in front of a bookshelf" style="background:linear-gradient(180deg,#6c5a4a 0%,#8b7b68 55%,#e6e1da 75%,#cfc9c0)"></div>
  <h3>Publications</h3><div class="btn">Read more</div>
</div>
<div class="res" style="left:783px">
  <div class="img" role="img" aria-label="Person holding binders labelled policies" style="background:linear-gradient(120deg,#e8e8e8,#9a9a9a 50%,#3a3a3a)"></div>
  <h3>Practice Policies and Forms</h3><div class="btn">Read more</div>
</div>

<!-- contact -->
<section class="abs contact"></section>
<div class="photo" role="img" aria-label="Study with a desk, lamp and tall bookshelf" style="left:699px;top:3789px;width:430px;height:313px;background:linear-gradient(120deg,#e6e2da,#c9bfae 45%,#6e4a2e 70%,#c98a3d)"></div>
<h2 class="abs serif" style="left:174px;top:3930px;font-size:33px;color:#fff">Contact info</h2>
<p class="abs" style="left:174px;top:3987px;width:380px;font-size:10px;line-height:17px;color:#fff">If you are going to use a passage of Lorem Ipsum, ou need to be sure there isn't anything embarrassing</p>
<div class="abs ci" style="top:4060px"><div class="ic"><svg width="11" height="11" viewBox="0 0 11 11"><rect x="2" y="1" width="7" height="3" fill="#5082c3"/><rect x="1" y="4" width="9" height="5" rx="1" fill="#5082c3"/></svg></div><div><small>Fax</small><span>emarlowe@quietmail.com</span></div></div>
<div class="abs ci" style="top:4115px"><div class="ic"><svg width="11" height="11" viewBox="0 0 11 11"><path d="M2 1h2l1 3-1.3 1A6 6 0 0 0 6 7.3L7 6l3 1v2a1 1 0 0 1-1 1A8 8 0 0 1 1 2a1 1 0 0 1 1-1z" fill="#5082c3"/></svg></div><div><small>Phone number</small><span>+1 (415) 555-0182</span></div></div>
<div class="abs ci" style="top:4187px"><div class="ic"><svg width="10" height="12" viewBox="0 0 10 13"><path d="M5 0a4.5 4.5 0 0 0-4.5 4.5C.5 8 5 13 5 13s4.5-5 4.5-8.5A4.5 4.5 0 0 0 5 0z" fill="#5082c3"/><circle cx="5" cy="4.5" r="1.6" fill="#fff"/></svg></div><div><small>Location</small><span style="display:block;width:160px">240 Alder St #312, San Francisco, CA 94104, United</span></div></div>
<div class="abs hours">
  <h4>Working time</h4>
  <div class="row"><span>Monday - Friday:</span><span>8 am - 5 pm</span></div>
  <div class="row"><span>Saturday</span><span>9 am - 2 pm</span></div>
  <div class="row"><span>Sunday</span><span>closed</span></div>
</div>
<div class="abs" style="left:0;width:1200px;text-align:center;top:4307px;font-size:10px;color:#fff">Copyright © 2023 Elliot Marlowe, Psy.D. | California Licensed Psychologist PSY 48211 | Analytical Psychologist Licensed Clinical Psychologist</div>

</body>
</html>
```